Infographic: Captive Insurance for the Cannabis Industry

I need an infographic designed for the attached article. The resulting document will be used in B2B content marketing and education, so it must be professional and clean and not an exercise in art. Colors used should be those of my logo found in the signature: blue, yellow & white. Design is up to the expert's discretion. I expect there will be a few iterations. ALSO: The chosen designer can expect many more projects using the same overall design, so it behooves you to participate. Please follow these directions and ask questions if unclear.

Target Market(s)

Business Owners, CFO's, CPAs Consultants, Commercial Real Estate Professionals

Font styles to use
Sans Serif

Requirements
Must have
• Clean professional design (not too overboard) using only the colors specified (see logo in signature- white, blue & gold/yellow)
• Images provided
• Call to action with link provided
• Signature block- use your discretion
• Everything you need is on the document
Should not have
• Too much clutter, wrong colors

```html
<!DOCTYPE html>
<html lang="en">
<head>
<meta charset="utf-8">
<title>Captive Insurance for the Cannabis Industry</title>
<link href="https://fonts.googleapis.com/css2?family=Montserrat:wght@700;800&family=Roboto:wght@400;500;700&family=Roboto+Condensed:wght@400;700&display=swap" rel="stylesheet">
<style>
:root{
  --blue:#0a4da2;
  --blue-dark:#083f86;
  --yellow:#fdcb3a;
  --white:#ffffff;
  --ink:#3d3d3d;
  --stage:#a8a8a8;
  --panel:#e9ecf1;
}
*{margin:0;padding:0;box-sizing:border-box}
html,body{width:966px;height:1200px;overflow:hidden}
body{background:var(--stage);font-family:"Roboto",sans-serif;color:var(--ink);position:relative}
.page{position:absolute;width:418px;height:540px;background:var(--white);overflow:hidden;box-shadow:0 2px 6px rgba(0,0,0,.25)}
.p1{left:60px;top:46px}.p2{left:493px;top:46px}.p3{left:60px;top:605px}.p4{left:493px;top:605px}
.abs{position:absolute}
.photo{position:absolute}
.body-text{font-size:6.3px;line-height:1.32;color:var(--ink)}
.body-text p+p{margin-top:3px}

/* page 1 */
.p1-title{left:11px;top:12px;font-family:"Montserrat",sans-serif;font-weight:800;font-size:15.5px;line-height:1.02;color:#111;letter-spacing:.3px}
.p1-sub{left:0;top:46px;width:238px;height:36px;background:var(--blue);clip-path:polygon(0 0,100% 0,94% 100%,0 100%);color:var(--white);font-weight:700;font-size:7.2px;line-height:1.3;padding:5px 20px 0 11px;text-transform:uppercase}
.p1-aside{left:236px;top:0;width:182px;height:62px;background:var(--yellow);clip-path:polygon(12% 0,100% 0,100% 100%,0 100%);font-size:6.3px;line-height:1.3;color:var(--ink);padding:14px 8px 0 26px;text-align:center}
.p1-lead{left:15px;top:108px;width:380px;color:var(--blue);font-weight:700;font-size:11px;line-height:1.3}
.p1-intro{left:15px;top:135px;width:380px}
.p1-photo{left:15px;top:212px;width:377px;height:170px;background:linear-gradient(120deg,#3a3a3a 0%,#6e6e6e 35%,#f2ea3c 55%,#d9d13a 75%,#5a5a5a 100%)}
.col-head{color:var(--blue);font-weight:700;font-size:8px;margin-bottom:5px}
.p1-colA{left:15px;top:394px;width:170px}
.p1-colB{left:232px;top:394px;width:160px}
.p1-divider{left:211px;top:396px;width:1px;height:80px;background:#c7c7c7}

/* page 2 */
.hdr-blue{left:0;top:0;width:418px;height:118px;background:var(--blue)}
.hdr-text{left:20px;top:19px;width:378px;text-align:center;font-weight:700;font-size:10.5px;line-height:1.3;text-transform:uppercase}
.hdr-blue .hdr-text,.p2 .hdr-text,.p4 .hdr-text{color:var(--white)}
.p2-photo{left:20px;top:74px;width:377px;height:129px;background:linear-gradient(100deg,#d7cf8a 0%,#e3d23a 30%,#9bb04a 55%,#e8dc6e 80%,#c8c08a 100%)}
.benefit{left:0;width:418px}
.benefit h3{position:relative;font-family:"Roboto Condensed",sans-serif;font-weight:700;font-size:12.5px;color:var(--blue);padding-left:25px;margin-bottom:2px}
.benefit h3::before{content:"";position:absolute;left:0;top:4px;width:18px;height:8px;background:var(--blue)}
.benefit ul{list-style:none;padding-left:30px}
.benefit li,.dot-list li{position:relative;font-family:"Roboto Condensed",sans-serif;font-size:8.3px;line-height:1.17;color:#222}
.benefit li::before,.dot-list li::before{content:"";position:absolute;left:-5px;top:3.5px;width:3px;height:3px;border-radius:50%;background:var(--yellow)}
.p2-b1{top:220px}.p2-b2{top:286px}.p2-b3{top:338px}
.gaps-box{left:181px;top:388px;width:237px;height:90px;background:var(--blue);padding:4px 10px 0 57px}
.gaps-box h4{color:var(--yellow);font-weight:500;font-size:8.3px;margin-bottom:2px}
.gaps-box ul{list-style:none;padding-left:7px}
.gaps-box li{position:relative;color:var(--white);font-size:6.4px;line-height:1.27}
.gaps-box li::before{content:"";position:absolute;left:-6px;top:2.3px;width:3px;height:3px;border-radius:50%;background:var(--yellow)}
.gaps-callout{left:23px;top:403px;width:198px;height:63px;background:var(--yellow);color:var(--blue);font-weight:700;font-size:8.3px;line-height:1.28;padding:6px 10px}

/* page 3 */
.hdr-yellow{left:0;top:0;width:418px;height:112px;background:var(--yellow)}
.p3 .hdr-text{color:var(--blue);font-size:11.6px;top:19px}
.p3-photo{left:19px;top:83px;width:378px;height:211px;background:linear-gradient(160deg,#f2f4ef 0%,#a9c48f 30%,#5f8a45 55%,#e9ecef 75%,#7ea25d 100%)}
.p3-banner{left:22px;top:292px;width:372px;height:40px;background:var(--blue);color:var(--white);text-align:center;font-weight:500;font-size:11px;line-height:1.3;padding-top:5px}
.p3-banner em{font-style:normal;color:var(--yellow)}
.sector-panel{left:22px;top:343px;width:372px;height:70px;background:var(--panel);display:flex;align-items:center;padding:0 8px}
.sector-col{list-style:none;padding-left:10px}
.sector-col li{position:relative;color:var(--blue);font-weight:500;font-size:15.5px;line-height:1.14}
.sector-col li::before{content:"";position:absolute;left:-8px;top:8px;width:4px;height:4px;border-radius:50%;background:var(--yellow)}
.sector-col+.sector-col{border-left:1px solid #b9bec6;margin-left:10px;padding-left:20px}
.sector-col+.sector-col li::before{left:-9px}
.p3-close{left:22px;top:424px;width:372px;font-size:6.9px}

/* page 4 */
.hdr-blue.tall{height:112px}
.p4 .hdr-text{font-size:10.8px;top:18px}
.p4 .hdr-text em{font-style:normal;color:var(--yellow)}
.hdr-rule{left:185px;top:80px;width:48px;height:2px;background:var(--yellow)}
.p4-photo{left:19px;top:89px;width:378px;height:222px;background:linear-gradient(135deg,#f7f7f5 0%,#e9e6e0 40%,#c8b59a 70%,#8a7a5a 100%)}
.p4-lead{left:22px;top:319px;color:var(--blue);font-weight:700;font-size:6.2px}
.dot-list{list-style:none;padding-left:7px}
.p4-list{left:22px;top:329px}
.p4-list li{font-family:"Roboto",sans-serif;font-size:7.2px;line-height:1.3;color:var(--ink)}
.p4-list li::before{top:3px}
.p4-highlight{left:22px;top:375px;width:363px;height:21px;background:var(--yellow);color:var(--blue);font-weight:700;font-size:7px;line-height:1.2;padding:2px 6px}
.p4-close{left:22px;top:402px;width:370px;font-size:7px}
.headshot{left:21px;top:438px;width:53px;height:55px;background:linear-gradient(160deg,#5e7790 0%,#c9b8a8 60%,#8aa0b5 100%)}
.signoff{left:80px;top:467px;line-height:1.1}
.signoff strong{display:block;color:var(--blue);font-size:7.5px}
.signoff span{display:block;font-size:6px;color:#555}

/* call to action footer */
.cta{position:absolute;left:0;top:496px;width:418px;height:44px}
.cta-yellow{position:absolute;left:0;top:0;width:212px;height:44px;background:var(--yellow);clip-path:polygon(0 0,93% 0,100% 100%,0 100%);padding:3px 0 0 10px}
.cta-q{font-size:6px;color:#555}
.cta-link{font-size:7.6px;color:var(--blue);font-weight:500;margin-top:-1px}
.cta-url{position:absolute;left:10px;top:24px;width:192px;height:15px;background:var(--white);font-size:5.9px;font-weight:700;color:var(--blue-dark);padding:4px 0 0 3px;white-space:nowrap}
.cta-url svg{position:absolute;right:2px;top:2px}
.cta-mail{position:absolute;left:202px;top:16px;width:136px;height:28px;background:var(--blue);clip-path:polygon(7% 0,100% 0,93% 100%,0 100%);color:var(--white);font-size:6.6px;font-weight:500;display:flex;align-items:center;padding-left:18px;gap:4px}
.mail-ic{width:10px;height:10px;border-radius:50%;background:var(--yellow);display:flex;align-items:center;justify-content:center}
.brand{position:absolute;left:346px;top:12px;width:66px;display:flex;align-items:center;gap:3px}
.brand-mark{width:6px;height:6px;background:var(--yellow);flex:none}
.brand-name{font-weight:700;font-size:7.4px;line-height:1.05;color:var(--blue);letter-spacing:.8px}
</style>
</head>
<body>

<!-- Page 1 -->
<section class="page p1">
  <div class="abs p1-aside">Cannabis is illegal under federal law, despite being legal to cultivate and sell medical marijuana in most states. The cannabis industry suffers from many gray areas because of the frequent conflicting treatments of the industry between state and federal laws.</div>
  <h1 class="abs p1-title">CAPTIVE INSURANCE FOR<br>THE CANNABIS INDUSTRY:</h1>
  <div class="abs p1-sub">A uniquely powerful approach to manage money and protect assets in an industry that isn't supported by the US banking system</div>
  <h2 class="abs p1-lead">One of the many hurdles facing Cannabis companies today is obtaining adequate business insurance.</h2>
  <div class="abs p1-intro body-text">
    <p>Because marijuana continues to be illegal under federal law, many traditional insurance companies have withdrawn from the cannabis market, following a leading London underwriting market's decision to get out of the industry altogether in 2015. The remaining insurance companies in the cannabis space charge notably higher premiums than for traditional businesses in response to the uncertainty of federal laws.</p>
    <p>Additionally, cannabis companies can find it difficult to insure certain risks. For example, many cannabis companies have taken massive hits from the hurricanes of 2017 and the current California wildfires.</p>
    <p>Given all the challenges facing cannabis companies today, is there a possible solution? How do you manage money and protect assets in an industry which isn't fully supported by the US banking system?</p>
  </div>
  <div class="photo p1-photo" role="img" aria-label="Photo of a hand in a business suit writing 'Are you covered?' over a bright yellow marker stroke"></div>
  <div class="abs p1-colA body-text">
    <h3 class="col-head">Enter captive insurance.</h3>
    <p>The challenges described above have created a perfect storm for cannabis companies to consider captive insurance companies. Popularized in the 1950's, captive insurance is a great alternative when the traditional insurance market fails the insured by being too costly, leaving too many gaps in coverage, or is unavailable.</p>
  </div>
  <div class="abs p1-divider"></div>
  <div class="abs p1-colB body-text">
    <h3 class="col-head">What is a Captive Insurance Company?</h3>
    <p>A wholly owned subsidiary company that provides risk-mitigation services for its parent company, or group of related companies. It's a form of corporate self-insurance. The financial benefits must be weighed against the administrative costs, and the insurance policies are subject to the same compliance rules as all insurance companies.</p>
  </div>
  <footer class="cta">
    <div class="cta-yellow"><p class="cta-q">Not sure if Captive Insurance is for you?</p><p class="cta-link">Click here to schedule a time to talk.</p>
      <div class="cta-url">https://www.northfieldcapital.com/cannabisdiscovery<svg width="9" height="11" viewBox="0 0 9 11"><path d="M1 1 L1 9 L3 7 L5 10 L6.5 9.3 L4.5 6.3 L7.5 6.3 Z" fill="#0a4da2"/></svg></div>
    </div>
    <div class="cta-mail"><span class="mail-ic"><svg width="6" height="5" viewBox="0 0 6 5"><rect x=".3" y=".3" width="5.4" height="4.4" fill="none" stroke="#0a4da2" stroke-width=".7"/><path d="M.3 .3 L3 2.7 L5.7 .3" fill="none" stroke="#0a4da2" stroke-width=".7"/></svg></span>daniel@northfieldcapital.com</div>
    <div class="brand"><span class="brand-mark"></span><span class="brand-name">NORTHFIELD<br>CAPITAL</span></div>
  </footer>
</section>

<!-- Page 2 -->
<section class="page p2">
  <div class="abs hdr-blue"></div>
  <h2 class="abs hdr-text">Given the nature of the industry and the challenges facing it as described above, captive insurance is an ideal solution for the cannabis industry.</h2>
  <div class="photo p2-photo" role="img" aria-label="Photo of cannabis leaves resting on a spread of US dollar bills"></div>
  <div class="abs benefit p2-b1">
    <h3>Some of the benefits of captive insurance regarding risk management:</h3>
    <ul>
      <li>Increased insurance coverage</li>
      <li>Increased efficiency of coverage – completely customized to pay only for what is needed</li>
      <li>Full claim control</li>
      <li>Improved underwriting flexibility to react to changing markets</li>
      <li>Access to the reinsurance market</li>
    </ul>
  </div>
  <div class="abs benefit p2-b2">
    <h3>Reduced insurance costs:</h3>
    <ul>
      <li>Eliminate paying for overhead and marketing costs charged by big insurance companies</li>
      <li>Provides negotiation leverage with traditional insurance companies</li>
      <li>Creates potential awareness within an organization for more efficient loss prevention practices</li>
    </ul>
  </div>
  <div class="abs benefit p2-b3">
    <h3>Improved Cash Flow:</h3>
    <ul>
      <li>Retain insurance premium dollars within the business to use at the owner's discretion</li>
      <li>Increase investment income</li>
      <li>Potential tax benefits (280E)</li>
    </ul>
  </div>
  <div class="abs gaps-box">
    <h4>These include but are not limited to:</h4>
    <ul>
      <li>Crop insurance</li>
      <li>Property and business interruption insurance</li>
      <li>Cyber attacks</li>
      <li>Auto &amp; product liability</li>
      <li>Worker's compensation</li>
      <li>Worker's personal injury</li>
      <li>Intellectual property</li>
      <li>Legal defense</li>
      <li>Employee theft</li>
    </ul>
  </div>
  <div class="abs gaps-callout">There are many examples of gaps not covered by traditional insurance companies that captive insurance can be customized to address for the cannabis industry.</div>
  <footer class="cta">
    <div class="cta-yellow"><p class="cta-q">Not sure if Captive Insurance is for you?</p><p class="cta-link">Click here to schedule a time to talk.</p>
      <div class="cta-url">https://www.northfieldcapital.com/cannabisdiscovery<svg width="9" height="11" viewBox="0 0 9 11"><path d="M1 1 L1 9 L3 7 L5 10 L6.5 9.3 L4.5 6.3 L7.5 6.3 Z" fill="#0a4da2"/></svg></div>
    </div>
    <div class="cta-mail"><span class="mail-ic"><svg width="6" height="5" viewBox="0 0 6 5"><rect x=".3" y=".3" width="5.4" height="4.4" fill="none" stroke="#0a4da2" stroke-width=".7"/><path d="M.3 .3 L3 2.7 L5.7 .3" fill="none" stroke="#0a4da2" stroke-width=".7"/></svg></span>daniel@northfieldcapital.com</div>
    <div class="brand"><span class="brand-mark"></span><span class="brand-name">NORTHFIELD<br>CAPITAL</span></div>
  </footer>
</section>

<!-- Page 3 -->
<section class="page p3">
  <div class="abs hdr-yellow"></div>
  <h2 class="abs hdr-text">The key point is, as mentioned previously, is that captive insurance benefits from complete customization by the owner.</h2>
  <div class="photo p3-photo" role="img" aria-label="Photo of a scientist in a white lab coat inspecting tall cannabis plants"></div>
  <div class="abs p3-banner">Captive insurance is not only a potential option for growers,<br>but any business that <em>“touches”</em> marijuana, including:</div>
  <div class="abs sector-panel">
    <ul class="sector-col" style="padding-top:10px"><li>Cultivators</li><li>Distributors</li></ul>
    <ul class="sector-col"><li>Dispensaries</li><li>Doctors</li><li>Property owners</li></ul>
    <ul class="sector-col" style="padding-top:4px"><li>Events</li><li>Supplies</li></ul>
  </div>
  <p class="abs p3-close body-text">Despite having made a case for the consideration of captive insurance by companies in the cannabis niche, this is not a slam dunk solution and challenges still exist because marijuana is still illegal under federal law. Additionally, creating the captive company can be very complex. Therefore, any captive must be developed in conjunction with a qualified captive manager who knows the qualified jurisdictions that can license a captive insurance company for the cannabis industry.</p>
  <footer class="cta">
    <div class="cta-yellow"><p class="cta-q">Not sure if Captive Insurance is for you?</p><p class="cta-link">Click here to schedule a time to talk.</p>
      <div class="cta-url">https://www.northfieldcapital.com/cannabisdiscovery<svg width="9" height="11" viewBox="0 0 9 11"><path d="M1 1 L1 9 L3 7 L5 10 L6.5 9.3 L4.5 6.3 L7.5 6.3 Z" fill="#0a4da2"/></svg></div>
    </div>
    <div class="cta-mail"><span class="mail-ic"><svg width="6" height="5" viewBox="0 0 6 5"><rect x=".3" y=".3" width="5.4" height="4.4" fill="none" stroke="#0a4da2" stroke-width=".7"/><path d="M.3 .3 L3 2.7 L5.7 .3" fill="none" stroke="#0a4da2" stroke-width=".7"/></svg></span>daniel@northfieldcapital.com</div>
    <div class="brand"><span class="brand-mark"></span><span class="brand-name">NORTHFIELD<br>CAPITAL</span></div>
  </footer>
</section>

<!-- Page 4 -->
<section class="page p4">
  <div class="abs hdr-blue tall"></div>
  <h2 class="abs hdr-text">Having said that, the fact that most <em>Top 500 companies</em> have some form of captive insurance should be an indicator that captive insurance should at least be understood as it pertains to most companies.</h2>
  <div class="abs hdr-rule"></div>
  <div class="photo p4-photo" role="img" aria-label="Photo of a doctor writing on a clipboard while holding a cannabis bud"></div>
  <p class="abs p4-lead">The best types of cannabis companies that should consider captive insurance have the following properties:</p>
  <ul class="abs dot-list p4-list">
    <li>Positive cash flow</li>
    <li>Relatively few claims</li>
    <li>Strong risk management</li>
    <li>Require coverage for multiple entities to distribute risk</li>
  </ul>
  <p class="abs p4-highlight">It is possible for multiple companies to pool their resources and form a group captive insurance company.</p>
  <p class="abs p4-close body-text">Hopefully, this information has, at the very least, increased the awareness of what is possible for cannabis related businesses. The search for finding the right financial investment and insurance that will perform for your cannabis related business may be over!</p>
  <div class="photo headshot" role="img" aria-label="Portrait photo of the owner"></div>
  <div class="abs signoff"><strong>Daniel Hartwell</strong><span>Northfield Capital,</span><span>Owner</span></div>
  <footer class="cta">
    <div class="cta-yellow"><p class="cta-q">Not sure if Captive Insurance is for you?</p><p class="cta-link">Click here to schedule a time to talk.</p>
      <div class="cta-url">https://www.northfieldcapital.com/cannabisdiscovery<svg width="9" height="11" viewBox="0 0 9 11"><path d="M1 1 L1 9 L3 7 L5 10 L6.5 9.3 L4.5 6.3 L7.5 6.3 Z" fill="#0a4da2"/></svg></div>
    </div>
    <div class="cta-mail"><span class="mail-ic"><svg width="6" height="5" viewBox="0 0 6 5"><rect x=".3" y=".3" width="5.4" height="4.4" fill="none" stroke="#0a4da2" stroke-width=".7"/><path d="M.3 .3 L3 2.7 L5.7 .3" fill="none" stroke="#0a4da2" stroke-width=".7"/></svg></span>daniel@northfieldcapital.com</div>
    <div class="brand"><span class="brand-mark"></span><span class="brand-name">NORTHFIELD<br>CAPITAL</span></div>
  </footer>
</section>

</body>
</html>
```